Store Signage for New Location

I need a banner for my new location. It needs to communicate 1: our name, 2: our phone number 3: our message. This is going to be a 7 foot wide banner that is 4 feet tall. It needs to be a very high resolution design so it prints properly.

Our phone number is (913) 548-1907

Our Message: The HONEST alternative to the dealer.

Or: Your Honest Auto Service Center

"Honest" is our key word here.

Target Market(s)

Drive-by traffic.

Industry/Entity Type

Auto Repair

Requirements
Must have
• The name of our business: Tall Pine Auto Repair
• Our phone number: (913) 548-1907
• Our message: The HONEST alternative to the dealership.
• or: Your Honest Service Center
Nice to have
• I really just need a clean layout using the uploaded logo and font. It needs to be highly visible as a sign that is seen by drive-by traffic.
• I'd like the color scheme to be the same as what I have, however, you're more than welcome to add detail and color as needed.

```html
<!DOCTYPE html>
<html lang="en">
<head>
<meta charset="utf-8">
<title>Tall Pine Auto Repair – Banner</title>
<link rel="stylesheet" href="https://fonts.googleapis.com/css2?family=Exo+2:ital,wght@1,900&family=Montserrat:wght@800;900&family=Oswald:wght@500&display=swap">
<style>
  :root {
    --yellow: #ffec00;
    --ink: #111111;
    --white: #ffffff;
    --gray-dark: #3a3a3a;
    --gray-mid: #6e6e6e;
    --purple-light: #a9a3d6;
    --purple: #6b60b3;
    --purple-deep: #4e4398;
  }
  html, body {
    margin: 0;
    padding: 0;
    overflow: hidden;
    background: #ffffff;
  }
  .banner {
    position: relative;
    width: 1200px;
    height: 686px;
    overflow: hidden;
    background: linear-gradient(90deg, var(--gray-dark) 0%, var(--gray-mid) 55%, #8a8a8a 100%);
  }
  .banner__art {
    position: absolute;
    inset: 0;
    width: 1200px;
    height: 686px;
  }
  .business-name {
    position: absolute;
    right: 26px;
    top: 78px;
    margin: 0;
    font-family: "Exo 2", sans-serif;
    font-style: italic;
    font-weight: 900;
    font-size: 55px;
    letter-spacing: 0.5px;
    color: var(--ink);
    text-shadow: 2px 3px 4px rgba(0,0,0,0.35);
    white-space: nowrap;
  }
  .message {
    position: absolute;
    left: 79px;
    top: 270px;
    margin: 0;
    line-height: 1;
  }
  .message__line {
    display: block;
    font-family: "Oswald", sans-serif;
    font-weight: 500;
    font-size: 76px;
    line-height: 74px;
    color: var(--white);
    text-transform: uppercase;
  }
  .message__key {
    display: block;
    font-family: "Montserrat", sans-serif;
    font-weight: 900;
    font-size: 117px;
    line-height: 104px;
    letter-spacing: -2px;
    color: var(--yellow);
    margin: 0 0 4px -4px;
  }
  .phone {
    position: absolute;
    left: 79px;
    top: 592px;
    margin: 0;
    font-family: "Montserrat", sans-serif;
    font-weight: 800;
    font-size: 66px;
    line-height: 1;
    color: var(--yellow);
    white-space: nowrap;
  }
</style>
</head>
<body>
<main class="banner">
  <svg class="banner__art" viewBox="0 0 1470 840" preserveAspectRatio="none" aria-hidden="false">
    <defs>
      <linearGradient id="silver" x1="0" y1="0" x2="1" y2="1">
        <stop offset="0" stop-color="#f2f2f2"/>
        <stop offset="1" stop-color="#9a9a9a"/>
      </linearGradient>
      <linearGradient id="silver-inner" x1="0" y1="0" x2="0" y2="1">
        <stop offset="0" stop-color="#e6e6e6"/>
        <stop offset="1" stop-color="#bdbdbd"/>
      </linearGradient>
      <linearGradient id="cross-fill" x1="0" y1="0" x2="1" y2="1">
        <stop offset="0" stop-color="#8f87c9"/>
        <stop offset="1" stop-color="#5a4fa2"/>
      </linearGradient>
      <radialGradient id="vehicle-tones" cx="0.55" cy="0.45" r="0.6">
        <stop offset="0" stop-color="#f3c51a"/>
        <stop offset="0.55" stop-color="#c99a10"/>
        <stop offset="0.8" stop-color="#4a4a4a"/>
        <stop offset="1" stop-color="#0d0d0d"/>
      </radialGradient>
    </defs>

    <!-- header band -->
    <rect class="header-band" x="0" y="0" width="1470" height="322" fill="var(--yellow)"/>

    <!-- brand badge -->
    <circle class="brand-badge" cx="200" cy="160" r="135" fill="url(#silver)"/>
    <circle class="brand-badge__face" cx="200" cy="160" r="122" fill="url(#silver-inner)"/>

    <!-- speed stripes -->
    <g class="speed-stripes" fill="#262626">
      <polygon points="450,213 650,213 630,242 430,242"/>
      <polygon points="685,213 790,213 770,242 665,242"/>
      <polygon points="800,213 870,213 850,242 780,242"/>
      <polygon points="880,213 915,213 895,242 860,242"/>
      <polygon points="925,213 935,213 915,242 905,242"/>
      <polygon points="415,258 630,258 610,285 395,285"/>
      <polygon points="660,258 745,258 725,285 640,285"/>
      <polygon points="775,258 825,258 805,285 755,285"/>
      <polygon points="855,258 870,258 850,285 835,285"/>
      <polygon points="895,258 905,258 885,285 875,285"/>
      <polygon points="1315,213 1340,213 1320,242 1295,242"/>
      <polygon points="1370,213 1385,213 1365,242 1350,242"/>
      <polygon points="1415,213 1450,213 1430,242 1395,242"/>
      <polygon points="1288,258 1310,258 1290,285 1268,285"/>
      <polygon points="1340,258 1355,258 1335,285 1320,285"/>
      <polygon points="1385,258 1425,258 1405,285 1365,285"/>
    </g>

    <!-- service cross -->
    <g class="service-cross" fill="url(#cross-fill)" stroke="var(--purple-light)" stroke-width="6">
      <rect x="998" y="205" width="200" height="615" rx="26"/>
      <rect x="845" y="375" width="610" height="200" rx="26"/>
    </g>
    <circle class="service-cross__ring" cx="1100" cy="462" r="205" fill="var(--purple-light)"/>
    <circle class="service-cross__ring-inner" cx="1100" cy="462" r="192" fill="var(--purple)"/>
    <circle class="vehicle-photo" cx="1100" cy="462" r="180" fill="url(#vehicle-tones)"
            role="img" aria-label="Photo of a yellow sports car front with black racing stripes"/>
  </svg>

  <h1 class="business-name">Tall Pine Auto Repair</h1>

  <h2 class="message">
    <span class="message__line">The</span>
    <span class="message__key">HONEST</span>
    <span class="message__line">Alternative</span>
    <span class="message__line">to a Dealer</span>
  </h2>

  <p class="phone">(913) 548-1907</p>
</main>
</body>
</html>
```